web site update

I want to get a better website for a small high end remodeling and construction company
I currently have a web site but you will find that it is not good.
www.pelbrookhaven.com
We are a high end construction / remodeling company that has been in business since 2003. We primarily work in the mid peninsula of the bay area. Most of our clientele are very educated captains of industry. This group is still the target client.
I had my logo designed by Vellum Forge a few years ago and I do like it, I like the orange and black or orange a blue. I don’t have a lot of content on hand as far as professional photographs.
Number of pages not sure and are open to: design pages vs full function website
I think what I am after is a web presence that will seal the deal as we are getting high referrals from past clients.
Construction
1 page

```html
<!DOCTYPE html>
<html lang="en">
<head>
<meta charset="utf-8">
<title>Pelbrook Haven Remodeling</title>
<link href="https://fonts.googleapis.com/css2?family=Roboto:ital,wght@0,300;0,400;0,500;0,700;1,900&display=swap" rel="stylesheet">
<style>
:root{
  --orange:#ff6600;
  --black:#0d0d0d;
  --ink:#222;
  --muted:#8a8a8a;
  --band:#eeeeee;
  --white:#fff;
}
*{box-sizing:border-box;margin:0;padding:0}
html,body{width:1200px;height:3644px;overflow:hidden}
body{font-family:"Roboto",Arial,sans-serif;color:var(--ink);background:var(--white);position:relative}
section,header,footer,.topbar,.nav,.footer,.bottombar{position:relative;width:1200px}
.abs{position:absolute}
.btn{position:absolute;background:var(--orange);color:var(--white);font-size:20px;font-weight:400;display:flex;align-items:center;justify-content:center;letter-spacing:.5px}
.kicker{position:absolute;left:0;width:100%;text-align:center;font-size:22px;font-weight:400;color:#333}
.title{position:absolute;left:0;width:100%;text-align:center;font-size:42px;font-weight:400;color:var(--orange)}
.copy{position:absolute;font-size:13px;line-height:29px;color:var(--muted);text-align:center}
.photo{position:absolute;border:6px solid var(--white);box-shadow:0 0 0 2px #dcdcdc}

/* top bar */
.topbar{height:49px;background:var(--black)}
.social span{position:absolute;top:8px;width:32px;height:32px;border-radius:50%;border:2px solid var(--orange)}
.phone{position:absolute;right:78px;top:0;height:49px;display:flex;align-items:center;gap:14px;color:var(--white);font-size:22px}

/* nav */
.nav{height:101px;background:var(--white)}
.nav a{position:absolute;top:45px;font-size:17px;color:#333;text-decoration:none;letter-spacing:.3px}
.nav a.active{color:var(--orange)}
.brand{position:absolute;left:462px;top:-26px;width:276px;height:127px;background:var(--white);display:flex;align-items:center;justify-content:center;gap:12px;z-index:2}
.brand .mark{width:30px;height:30px;background:var(--orange)}
.brand .name{font-size:21px;font-weight:700;color:var(--black);line-height:25px;letter-spacing:.5px}

/* hero */
.hero{height:535px;overflow:hidden}
.hero-photo{position:absolute;inset:0;background:linear-gradient(90deg,#f7f5f1 0%,#ece6dc 30%,#b9a58a 52%,#6b4a31 70%,#4d3321 100%)}
.hero h1{position:absolute;left:78px;top:168px;font-size:41px;line-height:52px;font-weight:900;font-style:italic;color:var(--black)}

.about{height:437px}
.gallery{height:846px;background:var(--band)}
.tile{position:absolute;width:333px;height:224px;border:6px solid var(--white)}
.project{height:437px}
.arrow{position:absolute;width:38px;height:38px;border-radius:50%;display:flex;align-items:center;justify-content:center}
.services{height:500px;background:var(--band)}
.service{position:absolute;top:175px;width:483px;height:257px;border:4px solid var(--white)}
.service h3{position:absolute;top:86px;width:100%;text-align:center;font-size:24px;font-weight:400;color:var(--black)}
.clients{height:391px}

/* footer */
.footer{height:280px;background:var(--black);color:var(--white)}
.footer h4{position:absolute;top:43px;font-size:17px;font-weight:400;color:var(--orange);letter-spacing:1px}
.navlist{position:absolute;left:362px;top:88px;list-style:none}
.navlist li{font-size:14px;line-height:30px;display:flex;align-items:center;gap:16px}
.navlist li::before{content:"";width:9px;height:9px;border-radius:50%;background:var(--orange)}
.navlist li.active{color:var(--orange)}
.contact-row{position:absolute;left:607px;display:flex;gap:14px;font-size:14px;line-height:20px}
.blog-item{position:absolute;left:872px;display:flex;gap:16px;font-size:14px;line-height:19px}
.blog-item .thumb{width:52px;height:52px;border-radius:50%;background:radial-gradient(circle,#b89a7a,#6d5440);flex:none}
.blog-item b{color:var(--orange);font-weight:400;display:block}
.bottombar{height:68px;background:var(--black);border-top:1px solid #333;color:var(--white)}
.bottombar p{position:absolute;left:78px;top:25px;font-size:14px}
.bottombar p span{color:var(--orange);font-weight:700}
.footer-social{position:absolute;right:78px;top:26px;display:flex;gap:22px}
.footer-social span{width:16px;height:16px;border-radius:50%;background:var(--white);display:block}
.footer-social span:first-child{background:var(--orange)}
</style>
</head>
<body>

<header>
  <div class="topbar">
    <div class="social"><span style="left:78px"></span><span style="left:122px"></span><span style="left:166px"></span><span style="left:210px"></span></div>
    <div class="phone">
      <svg width="16" height="24" viewBox="0 0 16 24"><rect x="1" y="1" width="14" height="22" rx="2" fill="none" stroke="#ff6600" stroke-width="2"/><rect x="6" y="18" width="4" height="2" fill="#ff6600"/></svg>
      415.555.0142
    </div>
  </div>
  <nav class="nav">
    <svg class="abs" style="left:96px;top:12px" width="80" height="22" viewBox="0 0 80 22"><polyline points="2,20 40,3 78,20" fill="none" stroke="#ff6600" stroke-width="3"/></svg>
    <a class="active" style="left:112px">HOME</a>
    <a style="left:209px">ABOUT US</a>
    <a style="left:350px">SERVICES</a>
    <div class="brand"><span class="mark"></span><span class="name">PELBROOK HAVEN<br>REMODELING</span></div>
    <a style="left:768px">PROJECTS</a>
    <a style="left:899px">GALLERY</a>
    <a style="left:1016px">CONTACT US</a>
  </nav>
</header>

<section class="hero">
  <div class="hero-photo" role="img" aria-label="Bright modern kitchen with wood cabinets and stainless range"></div>
  <h1>LOREM IPSUM DOLOR AMET<br>SIMPLE DUMMY TEXT FOR<br>WRITTIG</h1>
  <div class="btn" style="left:78px;top:345px;width:255px;height:61px">CONTACT US NOW</div>
</section>

<section class="about">
  <div class="kicker" style="left:78px;width:500px;top:62px">ABOUT</div>
  <div class="title" style="left:78px;width:500px;top:100px">PELBROOK HAVEN</div>
  <p class="copy" style="left:118px;width:440px;top:160px">Lorem Ipsum is simply dummy text of the printing and typesetting industry. Lorem Ipsum has been the industry's standard dummy text ever since the 1500s, when an unknown printer took a galley of type and scrambled it to make a type specimen book. It has survived not only five centuries, but also the leap into electronic</p>
  <div class="btn" style="left:262px;top:311px;width:176px;height:63px">KNOW MORE</div>
  <div class="photo" role="img" aria-label="White contemporary kitchen with dining table" style="left:615px;top:61px;width:507px;height:311px;background:linear-gradient(135deg,#f4f4f4,#d8d8d8 55%,#8f8f8f)"></div>
</section>

<section class="gallery">
  <div class="kicker" style="top:63px">OUR</div>
  <div class="title" style="top:104px">GALLERY</div>
  <p class="copy" style="left:300px;width:600px;top:162px">You are welcome to check out our house gallery to make sure that this home is in prime condition which makes it a perfect living space</p>
  <div class="tile" role="img" aria-label="Dim living room" style="left:78px;top:238px;background:linear-gradient(135deg,#5a5a5a,#2a2a2a)">
    <svg class="abs" style="left:144px;top:88px" width="38" height="38" viewBox="0 0 38 38"><circle cx="15" cy="15" r="11" fill="none" stroke="#ff6600" stroke-width="4"/><line x1="23" y1="23" x2="35" y2="35" stroke="#ff6600" stroke-width="5"/><path d="M15 9v12M9 15h12" stroke="#ff6600" stroke-width="3"/></svg>
  </div>
  <div class="tile" role="img" aria-label="Open kitchen with bar stools" style="left:433px;top:238px;background:linear-gradient(160deg,#e6e2dc,#9a958e)"></div>
  <div class="tile" role="img" aria-label="Kitchen with cream cabinets and fridge" style="left:789px;top:238px;background:linear-gradient(160deg,#d9cbb4,#8a7150)"></div>
  <div class="tile" role="img" aria-label="Tiled walk-in shower" style="left:78px;top:474px;background:linear-gradient(160deg,#e4e6e8,#aab0b5)"></div>
  <div class="tile" role="img" aria-label="Bedroom with wooden bed" style="left:433px;top:474px;background:linear-gradient(160deg,#b98a5e,#5b3a22)"></div>
  <div class="tile" role="img" aria-label="Bathroom vanity with blue tiles" style="left:789px;top:474px;background:linear-gradient(160deg,#dfe4ee,#a9b4cf)"></div>
  <div class="btn" style="left:517px;top:719px;width:166px;height:61px">SHOW ALL</div>
</section>

<section class="project">
  <div class="photo" role="img" aria-label="Modern open-plan kitchen with glass walls" style="left:78px;top:63px;width:507px;height:308px;background:linear-gradient(135deg,#3b3b3b,#9fa6a0 55%,#5b6b4f)">
    <div class="arrow" style="left:6px;top:129px;background:var(--orange)"><svg width="12" height="14" viewBox="0 0 12 14"><path d="M9 1L3 7l6 6" fill="none" stroke="#000" stroke-width="2.5"/></svg></div>
    <div class="arrow" style="right:6px;top:129px;background:#111"><svg width="12" height="14" viewBox="0 0 12 14"><path d="M3 1l6 6-6 6" fill="none" stroke="#ff6600" stroke-width="2.5"/></svg></div>
  </div>
  <div class="kicker" style="left:600px;width:520px;top:72px">OUR</div>
  <div class="title" style="left:600px;width:520px;top:113px">PROJECT</div>
  <p class="copy" style="left:620px;width:480px;top:165px">Lorem Ipsum is simply dummy text of the printing and typesetting industry. Lorem Ipsum has been the industry's standard dummy text ever since the 1500s, when an unknown printer took a galley of type and scrambled it to make a type specimen book. It has survived not only five centuries, but also the leap into electronic</p>
  <div class="btn" style="left:770px;top:310px;width:176px;height:61px">KNOW MORE</div>
</section>

<section class="services">
  <div class="kicker" style="top:73px">OUR</div>
  <div class="title" style="top:115px">SERVICES</div>
  <div class="service" role="img" aria-label="High end construction interior" style="left:78px;background:linear-gradient(135deg,#e9e9e9,#a9a9a9)">
    <h3>HIGH END CONSTRUCTION</h3>
    <div class="btn" style="left:150px;top:125px;width:176px;height:58px">KNOW MORE</div>
  </div>
  <div class="service" role="img" aria-label="Remodeled bright kitchen" style="left:600px;background:linear-gradient(135deg,#e6eef2,#b9c7cf 60%,#8a5a36)">
    <h3>REMODELING</h3>
    <div class="btn" style="left:150px;top:125px;width:176px;height:58px">KNOW MORE</div>
  </div>
</section>

<section class="clients">
  <div class="kicker" style="top:62px">WHAT</div>
  <div class="title" style="top:104px">OUR CLIENT SAY</div>
  <p class="copy" style="left:180px;width:840px;top:158px">Lorem Ipsum is simply dummy text of the printing and typesetting industry. Lorem Ipsum has been the industry's standard dummy text ever since the 1500s, when an unknown printer took a galley of type and scrambled it to make a type specimen book. It has survived not only five centuries</p>
  <div class="abs" role="img" aria-label="Client portrait" style="left:467px;top:264px;width:62px;height:62px;border-radius:50%;border:3px solid #f2c9a8;background:radial-gradient(circle,#d9b08c,#7a5238)"></div>
  <div class="abs" style="left:545px;top:274px;font-size:15px;color:#555">— CLIENT NAME</div>
  <div class="abs" style="left:567px;top:300px;font-size:15px;color:#555">(something.com)</div>
</section>

<footer>
  <div class="footer">
    <div class="abs" style="left:82px;top:96px;display:flex;align-items:center;gap:12px">
      <span style="width:28px;height:28px;background:var(--orange);display:block"></span>
      <span style="font-size:20px;font-weight:700;line-height:24px">PELBROOK HAVEN<br>REMODELING</span>
    </div>
    <h4 style="left:360px">NAVIGATION</h4>
    <ul class="navlist">
      <li class="active">Home</li><li>About Us</li><li>Gallery</li><li>Projects</li><li>Contact Us</li>
    </ul>
    <h4 style="left:607px">GET IN TOUCH</h4>
    <div class="contact-row" style="top:94px">
      <svg width="16" height="22" viewBox="0 0 16 22"><path d="M8 21S2 12 2 8a6 6 0 0 1 12 0c0 4-6 13-6 13z" fill="none" stroke="#ff6600" stroke-width="2"/><circle cx="8" cy="8" r="2" fill="#ff6600"/></svg>
      <span>PELBROOK HAVEN<br>Lorem Ipsum is simply dummy<br>text for type and print</span>
    </div>
    <div class="contact-row" style="top:170px">
      <svg width="16" height="18" viewBox="0 0 16 18"><path d="M3 1h3l2 4-2 2c1 2 3 4 5 5l2-2 4 2v3c0 1-1 2-2 2C7 17 1 11 1 3c0-1 1-2 2-2z" fill="none" stroke="#ff6600" stroke-width="1.8"/></svg>
      <span>415 555 0142</span>
    </div>
    <div class="contact-row" style="top:204px">
      <svg width="16" height="14" viewBox="0 0 16 14"><rect x="1" y="1" width="14" height="12" fill="none" stroke="#ff6600" stroke-width="1.8"/><path d="M1 1l7 6 7-6" fill="none" stroke="#ff6600" stroke-width="1.8"/></svg>
      <span>info@pelbrookhaven.com</span>
    </div>
    <h4 style="left:874px">LATEST BLOG</h4>
    <div class="blog-item" style="top:86px">
      <div class="thumb" role="img" aria-label="Blog author photo"></div>
      <div><b>09/5</b>Lorem ipsum dolor sit<br>amet, consectetur adip...</div>
    </div>
    <div class="blog-item" style="top:162px">
      <div class="thumb" role="img" aria-label="Blog author photo"></div>
      <div><b>09/5</b>Lorem ipsum dolor sit<br>amet, consectetur adip...</div>
    </div>
  </div>
  <div class="bottombar">
    <p>© 2016 &nbsp;<span>PELBROOK HAVEN REMODELING</span>&nbsp; All Rights Reserved.</p>
    <div class="footer-social"><span></span><span></span><span></span><span></span></div>
  </div>
</footer>

</body>
</html>
```